Northgate Process Solutions

8.5 x 11 flyer one or two sides is fine. This will be used for a trade show. See message for details

Target Market(s)

Refineries and Petrochemical plants

Industry/Entity Type

Oil

```html
<!DOCTYPE html>
<html lang="en">
<head>
<meta charset="utf-8">
<title>Northgate Process Solutions – Trade Show Flyer</title>
<link rel="stylesheet" href="https://fonts.googleapis.com/css2?family=League+Spartan:wght@700;800;900&family=Jost:wght@400;500;600;700&display=swap">
<style>
  :root {
    --backdrop: #e6e6e6;
    --paper: #ffffff;
    --brand-green: #21952d;
    --ink: #0d0d0d;
    --white: #ffffff;
    --sky-top: #5eaaf6;
    --sky-low: #b7dcf6;
    --tank-grey: #c9ccce;
    --quay: #6f6a5c;
    --water: #2c5aa6;
  }
  * { margin: 0; padding: 0; box-sizing: border-box; }
  html, body { width: 1200px; height: 1091px; overflow: hidden; }
  body { background: var(--backdrop); position: relative; font-family: "Jost", sans-serif; }

  .flyer {
    position: absolute; left: 194px; top: 52px;
    width: 767px; height: 987px;
    background: var(--paper);
  }
  .masthead { position: absolute; left: 0; top: 0; width: 767px; height: 220px; }
  .masthead__name { font-family: "League Spartan", sans-serif; font-weight: 900; fill: var(--brand-green); }
  .masthead__sub { font-family: "League Spartan", sans-serif; font-weight: 900; fill: var(--ink); }
  .masthead__tagline { font-family: "League Spartan", sans-serif; font-weight: 800; fill: var(--brand-green); }

  .hero-photo {
    position: absolute; left: 77px; top: 256px; width: 659px; height: 500px;
    border-radius: 24px 48px 48px 0;
    background: linear-gradient(180deg, var(--sky-top) 0%, var(--sky-low) 48%, var(--tank-grey) 56%, var(--tank-grey) 66%, var(--quay) 72%, var(--quay) 76%, var(--water) 84%, #4a78c0 100%);
  }

  .info-panel {
    position: absolute; left: 10px; top: 440px; width: 373px; height: 431px;
    background: var(--brand-green); color: var(--white);
    border-radius: 30px 24px 30px 0;
    padding: 26px 0 0 37px;
  }
  .info-panel__heading { font-weight: 600; font-size: 20px; letter-spacing: 0.2px; line-height: 1; }
  .info-panel__text {
    width: 300px; font-size: 15px; line-height: 17.7px;
    margin-top: 12px; padding-left: 3px; hyphens: manual;
  }
  .info-panel__heading--services { margin-top: 58px; padding-left: 3px; }
  .info-panel__text strong { font-weight: 700; }

  .contact-block {
    position: absolute; left: 406px; top: 756px; width: 299px; height: 107px;
    background: var(--ink); color: var(--white);
    border-radius: 0 0 0 30px;
  }
  .contact-block__phone {
    position: absolute; left: 22px; top: 30px;
    display: flex; align-items: center; gap: 3px;
    font-family: "League Spartan", sans-serif; font-weight: 800; font-size: 35px; line-height: 1;
    white-space: nowrap;
  }
  .contact-block__phone svg { width: 24px; height: 24px; }
  .contact-block__web {
    position: absolute; left: 35px; top: 67px;
    font-size: 15px; font-weight: 500; letter-spacing: 5.6px;
    line-height: 1; white-space: nowrap;
  }

  .brand-sign {
    position: absolute; left: 70px; top: 898px;
    color: var(--ink); font-weight: 700; text-align: center; line-height: 1;
  }
  .brand-sign__main { font-size: 31px; }
  .brand-sign__sub { font-size: 12px; margin-top: 4px; }

  .experience { position: absolute; left: 424px; top: 903px; display: flex; align-items: center; gap: 21px; }
  .experience__badge { width: 35px; height: 33px; border: 2px solid var(--brand-green); }
  .experience__text {
    font-family: "League Spartan", sans-serif; font-weight: 800; font-size: 16px;
    line-height: 17px; color: var(--ink); letter-spacing: 0.2px;
  }
</style>
</head>
<body>
  <main class="flyer">
    <svg class="masthead" viewBox="0 0 767 220" aria-label="Northgate Process Solutions – Your strategic partner for productive solutions">
      <text class="masthead__name" x="111" y="143" font-size="88" textLength="569" lengthAdjust="spacingAndGlyphs">NORTHGATE</text>
      <text class="masthead__sub" x="111" y="183" font-size="46" textLength="569" lengthAdjust="spacingAndGlyphs">PROCESS SOLUTIONS</text>
      <text class="masthead__tagline" x="111" y="204" font-size="19.5" textLength="569" lengthAdjust="spacingAndGlyphs">YOUR STRATEGIC PARTNER FOR PRODUCTIVE SOLUTIONS</text>
    </svg>

    <div class="hero-photo" role="img" aria-label="Photograph of white industrial storage tanks at a waterfront terminal under a blue sky"></div>

    <section class="info-panel">
      <h2 class="info-panel__heading">ABOUT US</h2>
      <p class="info-panel__text">For 26 years, we've been your trusted partner worldwide in sourcing process residuals, byproducts, coproducts, and off-spec materi­als. Our mission is to promote environmental sustainability by repurposing and recycling these materials, reducing waste, and enhanc­ing resource efficiency.</p>
      <h2 class="info-panel__heading info-panel__heading--services">OUR SERVICES</h2>
      <p class="info-panel__text"><strong>We utilize a multi-faceted approach to support various industries using products like:</strong> Alcohols, Asphalt Flux , Bitumen, Crude Oil, Distillation Residue, Distressed Material, Glycols, Petroleum Hydrocarbons, Solvents, Tank Bottoms, Fuel, and More!</p>
    </section>

    <section class="contact-block">
      <div class="contact-block__phone">
        <svg viewBox="0 0 24 24" aria-hidden="true">
          <path fill="#fff" d="M6.6 10.8c1.4 2.8 3.8 5.1 6.6 6.6l2.2-2.2c.3-.3.7-.4 1-.2 1.1.4 2.3.6 3.6.6.6 0 1 .4 1 1V20c0 .6-.4 1-1 1C10.6 21 3 13.4 3 4c0-.6.4-1 1-1h3.5c.6 0 1 .4 1 1 0 1.3.2 2.5.6 3.6.1.3 0 .7-.2 1l-2.3 2.2z"/>
          <path fill="none" stroke="#fff" stroke-width="1.6" d="M14 3.5a7 7 0 0 1 6.5 6.5M14 7a3.5 3.5 0 0 1 3 3"/>
        </svg>
        <span>555-014-2000</span>
      </div>
      <div class="contact-block__web">WWW.NGPS-CO.COM</div>
    </section>

    <div class="brand-sign">
      <div class="brand-sign__main">Northgate</div>
      <div class="brand-sign__sub">Process Solutions</div>
    </div>

    <div class="experience">
      <div class="experience__badge" aria-hidden="true"></div>
      <p class="experience__text">26 YEARS OF TRUSTED<br>EXPERIENCE</p>
    </div>
  </main>
</body>
</html>
```